Kestwick Holdings AG needs web design

We need a website for a Swiss company: Kestwick Holdings AG. We offer our customers financial services such as advice and funds. We also have an interest rate calculator that we want to link to via a button on the website.

We are looking for a black and gold design. (Background: Black, Accents: Gold and White)
The design should convey security and growth. We have uploaded our logo in the attachment.
Font from the logo: Trajan Pro Regular

```html
<!DOCTYPE html>
<html lang="en">
<head>
<meta charset="utf-8">
<title>Kestwick Holdings AG</title>
<link href="https://fonts.googleapis.com/css2?family=Cinzel:wght@400;500;600&family=Poppins:wght@400;500&display=swap" rel="stylesheet">
<style>
:root{
  --black:#000;
  --ink:#0b0b0b;
  --graphite:#3b3b3b;
  --gold:#c9aa72;
  --gold-light:#ead5a5;
  --gold-dark:#a3844f;
  --white:#fff;
  --field:#fff;
  --gold-grad:linear-gradient(180deg,#ecd8a8 0%,#c9aa72 55%,#a98a55 100%);
}
*{box-sizing:border-box;margin:0;padding:0}
html,body{width:1200px;height:4124px;overflow:hidden;background:var(--black)}
body{position:relative;font-family:'Poppins',sans-serif;color:var(--white)}
.abs{position:absolute}
.serif{font-family:'Cinzel',serif}
.gold-text{color:var(--gold)}
.btn{position:absolute;display:flex;align-items:center;justify-content:center;border-radius:30px;background:var(--gold-grad);color:#2a2112;font-family:'Cinzel',serif;font-size:16px;letter-spacing:.5px}
.rule{position:absolute;height:4px;background:linear-gradient(90deg,var(--gold-light),var(--gold) 70%,transparent);border-radius:2px}
p.copy{font-size:13.4px;line-height:19.4px;color:var(--white)}

/* header / hero */
.hero{position:absolute;left:0;top:0;width:1200px;height:800px;overflow:hidden}
.hero-photo{position:absolute;inset:0;background:
  radial-gradient(ellipse at 70% 40%,rgba(170,170,170,.35),transparent 60%),
  radial-gradient(ellipse at 20% 60%,rgba(120,120,120,.35),transparent 55%),
  linear-gradient(180deg,#2a2a2a 0%,#3a3a3a 35%,#1c1c1c 70%,#000 100%)}
.brand{position:absolute;text-align:center;color:var(--gold);font-family:'Cinzel',serif}
.brand-top{position:absolute;left:150px;top:62px;width:220px;font-size:22px;line-height:26px}
.nav{position:absolute;top:112px;left:430px;display:flex;gap:0;font-family:'Cinzel',serif;font-size:15px}
.nav a{color:var(--white);text-decoration:none;position:absolute;white-space:nowrap}
.hero-welcome{position:absolute;top:308px;left:0;width:1200px;text-align:center;font-family:'Cinzel',serif;font-size:32px;color:var(--gold)}
.hero-title{position:absolute;top:360px;left:0;width:1200px;text-align:center;font-family:'Cinzel',serif;font-size:86px;line-height:100px;color:var(--gold)}
.hero-ag{position:absolute;top:458px;left:0;width:1200px;text-align:center;font-family:'Cinzel',serif;font-size:86px;line-height:100px;color:var(--gold)}

/* about */
.about{position:absolute;left:0;top:800px;width:1200px;height:593px;background:var(--black)}
.section-title{font-family:'Cinzel',serif;font-size:44px;color:var(--gold);position:absolute;white-space:nowrap}

/* why */
.why{position:absolute;left:0;top:1393px;width:1200px;height:581px;background:var(--graphite)}
.why-photo{position:absolute;left:140px;top:105px;width:417px;height:370px;border-radius:30px 0 30px 0;border:4px solid var(--gold);background:linear-gradient(135deg,#cfd4d6,#8a9095 45%,#4b4f53 80%,#2c2f33)}
.dots{position:absolute;left:100px;top:290px;width:280px;height:210px;background-image:radial-gradient(rgba(255,255,255,.18) 1px,transparent 1.2px);background-size:5px 5px}

/* services */
.services{position:absolute;left:0;top:1974px;width:1200px;height:650px;background:var(--black);overflow:hidden}
.svc-title{position:absolute;font-family:'Cinzel',serif;font-size:30px;color:var(--gold);text-align:right;white-space:nowrap}
.svc-copy{position:absolute;font-size:13.4px;line-height:19.4px;text-align:right}
.svc-icon{position:absolute;width:140px;height:140px;border-radius:50%;background:var(--gold-grad)}

/* news */
.news{position:absolute;left:0;top:2624px;width:1200px;height:904px;background:var(--graphite)}
.news-feature{position:absolute;left:131px;top:200px;width:488px;height:528px;border-radius:20px 0 20px 0;overflow:hidden;background:#1c1c1c}
.news-feature .photo{position:absolute;inset:0 0 110px 0;background:linear-gradient(160deg,#7b5a36,#c29a66 35%,#5f5c5a 65%,#2a2725)}
.news-feature .fade{position:absolute;left:0;right:0;top:300px;height:120px;background:linear-gradient(180deg,transparent,#1c1c1c)}
.news-feature h3{position:absolute;left:52px;top:416px;font-family:'Cinzel',serif;font-weight:400;font-size:28px;line-height:34px;color:var(--white)}
.news-card{position:absolute;left:660px;width:410px;height:257px;border:1.5px solid #8a8a8a;border-radius:20px 0 20px 0}
.news-card .oval{position:absolute;left:22px;top:18px;width:160px;height:210px;border-radius:50%}
.news-card .date{position:absolute;left:210px;top:48px;font-size:11px;color:var(--gold)}
.news-card h4{position:absolute;left:210px;top:76px;width:185px;font-family:'Cinzel',serif;font-weight:400;font-size:16.5px;line-height:20px;color:var(--gold)}
.news-card p{position:absolute;left:210px;top:150px;width:160px;font-size:11px;line-height:13.8px}

/* footer */
.footer{position:absolute;left:0;top:3528px;width:1200px;height:596px;background:var(--black)}
.contact-row{position:absolute;left:150px;display:flex;align-items:center;gap:20px;font-size:15.5px;line-height:22px}
.contact-row .ic{width:44px;height:44px;border-radius:50%;background:var(--gold-grad);display:flex;align-items:center;justify-content:center;flex:none}
.field{position:absolute;background:var(--field);border-radius:24px;color:#333;font-family:'Cinzel',serif;font-size:13px;padding:14px 18px}
.legal{position:absolute;left:0;top:4070px;width:1200px;text-align:center;font-family:'Cinzel',serif;font-size:12.5px}
</style>
</head>
<body>

<header class="hero">
  <div class="hero-photo" role="img" aria-label="Night city skyline with a rising financial chart overlay in silver tones"></div>
  <svg class="abs" style="left:0;top:0" width="1200" height="800" aria-hidden="true">
    <g stroke="rgba(255,255,255,.12)" stroke-dasharray="2 4">
      <line x1="0" y1="160" x2="1200" y2="160"/><line x1="0" y1="260" x2="1200" y2="260"/>
    </g>
    <polyline fill="none" stroke="rgba(255,255,255,.45)" stroke-width="2" points="0,520 150,470 260,500 380,430 500,470 620,360 720,390 800,250 860,300 950,190 1050,230 1120,120 1200,150"/>
  </svg>
  <div class="brand-top brand">KESTWICK<br>HOLDINGS AG</div>
  <div class="btn" style="left:760px;top:34px;width:288px;height:46px;font-size:15px">Interest Rate Calculator</div>
  <nav class="nav">
    <a style="left:0">HOME</a><a style="left:94px">SERVICES</a><a style="left:210px">ABOUT</a><a style="left:314px">NEWS</a><a style="left:404px">CUSTOMERS</a><a style="left:546px">CONTACT</a>
  </nav>
  <div class="hero-welcome">WELCOME TO</div>
  <div class="hero-title">KESTWICK HOLDINGS</div>
  <div class="rule" style="left:332px;top:502px;width:176px;height:4px;background:linear-gradient(270deg,var(--gold-light),var(--gold) 70%,transparent)"></div>
  <div class="hero-ag">AG</div>
  <div class="rule" style="left:692px;top:502px;width:176px"></div>
</header>

<section class="about">
  <h2 class="section-title" style="left:150px;top:140px">About AG</h2>
  <div class="rule" style="left:150px;top:202px;width:165px"></div>
  <p class="copy abs" style="left:150px;top:232px;width:440px">Lorem ipsum dolor sit amet, consectetur adipiscing elit, sed do eiusmod tempor incididunt ut labore et dolore magna aliquauis ipsum suspendisse ultrices gravida. Risus commodo viverra ma ecenas accumsan lacus vel facilisisorem ipsum dolor sit amet, consectetur adipiscing elit, sed do eiusmod tempor incididunt ut labore et dolore magna aliquauis ipsum suspendisse ultrices gravida. Risus commodo viverra maecenas accumsan lacus vel facilisismagna aliquauis ipsum sus.</p>
  <div class="btn" style="left:150px;top:425px;width:290px;height:47px">Interest Rate Calculator</div>
  <div class="abs serif gold-text" style="left:600px;top:160px;width:470px;text-align:center;font-size:64px;line-height:84px">KESTWICK<br>HOLDINGS AG</div>
</section>

<section class="why">
  <div class="dots"></div>
  <div class="why-photo" role="img" aria-label="Three colleagues reviewing documents around a laptop"></div>
  <h2 class="section-title" style="left:632px;top:118px">Why Choose Us</h2>
  <div class="rule" style="left:632px;top:180px;width:165px"></div>
  <p class="copy abs" style="left:632px;top:212px;width:440px">Lorem ipsum dolor sit amet, consectetur adipiscing elit, sed do eiusmod tempor incididunt ut labore et dolore magna aliquauis ipsum suspendisse ultrices gravida. Risus commodo viverra ma ecenas accumsan lacus vel facilisisorem ipsum dolor sit amet, consectetur adipiscing elit, sed do eiusmod tempor incididunt ut labore et dolore magna aliquauis ipsum suspendisse ultrices gravida. Risus commodo viverra maecenas accumsan lacus vel facilisismagna aliquauis ipsum sus.</p>
  <div class="btn" style="left:632px;top:403px;width:140px;height:47px">Read More</div>
</section>

<section class="services">
  <svg class="abs" style="left:0;top:0" width="1200" height="650" aria-hidden="true">
    <defs>
      <linearGradient id="svcPhoto" x1="0" y1="0" x2="1" y2="1">
        <stop offset="0" stop-color="#3a3530"/><stop offset=".5" stop-color="#6f7c8e"/><stop offset="1" stop-color="#9a8a78"/>
      </linearGradient>
    </defs>
    <path d="M790 0 C690 140 660 300 690 430 C710 530 760 600 800 650 L1200 650 L1200 0 Z" fill="#4a4a4a"/>
    <path d="M815 0 C720 140 690 300 718 430 C738 530 785 600 825 650 L1200 650 L1200 0 Z" fill="url(#svcPhoto)" role="img" aria-label="Blurred hands reviewing financial charts on paper"/>
  </svg>
  <div class="abs serif" style="left:873px;top:268px;font-size:44px;line-height:48px;color:var(--gold-light)">Our<br>Services</div>

  <div class="svc-title" style="right:562px;top:94px">Service 01</div>
  <p class="svc-copy" style="right:562px;top:150px;width:460px">Lorem ipsum dolor sit amet, consectetur adipiscing elit, sed do eiusmod tempor incididunt ut labore et dolore magna aliquauis ipsum suspendisse ultrices gravida. Risus commodo viverra</p>
  <div class="svc-icon" style="left:667px;top:100px"></div>
  <svg class="abs" style="left:707px;top:140px" width="60" height="60" fill="none" stroke="#1a1a1a" stroke-width="2" aria-hidden="true">
    <rect x="14" y="4" width="36" height="26" rx="3"/><line x1="20" y1="12" x2="44" y2="12"/><line x1="20" y1="19" x2="40" y2="19"/>
    <path d="M4 42 L16 36 L32 38 L46 32 L52 36 L36 48 L14 52 Z"/>
  </svg>

  <div class="svc-title" style="right:625px;top:256px">Service 02</div>
  <p class="svc-copy" style="right:625px;top:312px;width:460px">Lorem ipsum dolor sit amet, consectetur adipiscing elit, sed do eiusmod tempor incididunt ut labore et dolore magna aliquauis ipsum suspendisse ultrices gravida. Risus commodo viverra</p>
  <div class="svc-icon" style="left:610px;top:255px"></div>
  <svg class="abs" style="left:650px;top:295px" width="60" height="60" fill="none" stroke="#1a1a1a" stroke-width="2" aria-hidden="true">
    <circle cx="32" cy="20" r="14"/><text x="26" y="27" font-size="20" fill="#1a1a1a" stroke="none" font-family="Poppins,sans-serif">$</text>
    <path d="M4 44 L16 38 L30 40 L44 36 L50 40 L34 52 L12 54 Z"/>
  </svg>

  <div class="svc-title" style="right:562px;top:437px">Service 03</div>
  <p class="svc-copy" style="right:562px;top:493px;width:460px">Lorem ipsum dolor sit amet, consectetur adipiscing elit, sed do eiusmod tempor incididunt ut labore et dolore magna aliquauis ipsum suspendisse ultrices gravida. Risus commodo viverra</p>
  <div class="svc-icon" style="left:657px;top:420px"></div>
  <svg class="abs" style="left:697px;top:460px" width="60" height="60" fill="none" stroke="#1a1a1a" stroke-width="2" aria-hidden="true">
    <ellipse cx="18" cy="12" rx="14" ry="5"/><path d="M4 12 V40 M32 12 V24"/>
    <path d="M4 22 Q18 28 26 25 M4 31 Q18 37 24 34 M4 40 Q18 46 26 43"/>
    <circle cx="40" cy="38" r="14"/><text x="35" y="45" font-size="18" fill="#1a1a1a" stroke="none" font-family="Poppins,sans-serif">$</text>
  </svg>
</section>

<section class="news">
  <h2 class="section-title" style="left:0;width:1200px;text-align:center;top:82px;font-size:50px">Our Latest News</h2>
  <article class="news-feature">
    <div class="photo" role="img" aria-label="Team of four colleagues gathered around a laptop in an office"></div>
    <div class="fade"></div>
    <h3>Lorem ipsum do lor sit<br>loreamet, consecte</h3>
  </article>
  <article class="news-card" style="top:200px">
    <div class="oval" role="img" aria-label="Blue financial dashboard graphics" style="background:linear-gradient(135deg,#0e2a4a,#3a8cc8 50%,#0b1c33)"></div>
    <div class="date">Jan 18th, 2022</div>
    <h4>Lorem ipsum dlor sit loreametconse ctetur adipiscin.</h4>
    <p>Sed ut perspiciatis unde omnis iste natus error sit voluptatem accusantium doloremque laud antium, totam rem aperiam</p>
  </article>
  <article class="news-card" style="top:487px">
    <div class="oval" role="img" aria-label="Hand pointing a pen at printed charts" style="background:linear-gradient(135deg,#6b4a3a,#cfd6de 45%,#6f9ccc 80%,#e8ecf0)"></div>
    <div class="date">Jan 18th, 2022</div>
    <h4>Lorem ipsum dlor sit loreametconse ctetur adipiscin.</h4>
    <p>Sed ut perspiciatis unde omnis iste natus error sit voluptatem accusantium doloremque laud antium, totam rem aperiam</p>
  </article>
  <div class="btn" style="left:557px;top:802px;width:140px;height:47px">Read More</div>
</section>

<footer class="footer">
  <div class="brand" style="left:150px;top:84px;width:265px;font-size:26px;line-height:34px">KESTWICK<br>HOLDINGS AG</div>

  <div class="contact-row" style="top:246px">
    <span class="ic"><svg width="20" height="20" viewBox="0 0 24 24" fill="#1a1a1a" aria-hidden="true"><path d="M6.6 10.8a15 15 0 006.6 6.6l2.2-2.2c.3-.3.7-.4 1-.2 1.1.4 2.3.6 3.6.6.6 0 1 .4 1 1V20c0 .6-.4 1-1 1A17 17 0 013 4c0-.6.4-1 1-1h3.5c.6 0 1 .4 1 1 0 1.3.2 2.5.6 3.6.1.3 0 .7-.2 1z"/></svg></span>
    <span>Phone<br>+00 4410 2290</span>
  </div>
  <div class="contact-row" style="top:310px">
    <span class="ic"><svg width="18" height="14" viewBox="0 0 18 14" aria-hidden="true"><rect width="18" height="14" rx="2" fill="#1a1a1a"/><path d="M1 2 L9 8 L17 2" stroke="#c9aa72" stroke-width="1.5" fill="none"/></svg></span>
    <span>Email<br>info@kestwick-mail.com</span>
  </div>
  <div class="contact-row" style="top:374px">
    <span class="ic"><svg width="16" height="22" viewBox="0 0 16 22" aria-hidden="true"><path d="M8 0a8 8 0 018 8c0 6-8 14-8 14S0 14 0 8a8 8 0 018-8z" fill="#1a1a1a"/><circle cx="8" cy="8" r="3" fill="#c9aa72"/></svg></span>
    <span>Lindenweg 14<br>8001 Talbruck</span>
  </div>

  <h2 class="section-title" style="left:504px;top:70px;font-size:40px">Conatct Us</h2>
  <div class="field" style="left:496px;top:120px;width:269px;height:45px">Name:</div>
  <div class="field" style="left:779px;top:120px;width:269px;height:45px">Email:</div>
  <div class="field" style="left:496px;top:182px;width:269px;height:45px">Phone:</div>
  <div class="field" style="left:779px;top:182px;width:269px;height:45px">Subject:</div>
  <div class="field" style="left:496px;top:247px;width:552px;height:150px;padding-top:20px">Message:</div>
  <div class="btn" style="left:496px;top:417px;width:152px;height:50px;font-size:17px">Submit</div>

  <div class="abs" style="left:131px;top:517px;width:948px;height:1px;background:#6a6a6a"></div>
  <div class="legal" style="top:542px">© 2022 All Rights Reserved.Terms &amp; Conditions Privacy Policy</div>
</footer>

</body>
</html>
```